Modern Design for Eyecare business - Vision Center, Optometry, Eye Doctors, Health Care

Create a sleek, modern, sharp homepage design for a eyecare center in Oklahoma City, OK. The vision center provides eyecare health services along with prescription eyewear.

I have included the logo which should be the basis of the designs look and feel. No other imagery was given so feel free to include stock photos and illustrations that you believe give the design a fresh look.

Please do not include stock photos of people/humans

I have included a document that provides some verbiage for the design as well as the designs main navigation.

They have an existing website http://www.bluepineoptics.example/ but are not happy with it. The new design should be different than their existing design.

List of websites for inspiration:
http://www.harborfaith.example
https://www.meadowlenspartners.example
http://www.brightsmiledental.example/
https://www.keltro.example

Target Market(s)

all ages

industry: Health, Eyewear, Eyecare, Optometry

Industry/Entity Type

Health

Number of Pages Required

1 page

Requirements
Must have
• Light color scheme that matches logo colors.
• Sophisticated, sleek design that resembles the logo's style.
Nice to have
• Large, full width visual banner with a 'contact us, etc' call-to-action between header and homepage content
Should not have
• No stock images of people/humans.
• Other forms of stock photos/illustrations are fine.

```html
<!DOCTYPE html>
<html lang="en">
<head>
<meta charset="utf-8">
<title>Blue Pine Optics</title>
<link href="https://fonts.googleapis.com/css2?family=Cinzel:wght@400&family=Open+Sans:wght@400;600;700&family=Oswald:wght@400;500&family=Cormorant+Garamond:wght@500&display=swap" rel="stylesheet">
<style>
:root{
  --ink:#2f3b4a;
  --muted:#5a6470;
  --teal:#1ea7c6;
  --teal-dark:#1391ad;
  --orange:#f2703f;
  --purple:#3a2f8f;
  --nav:#5a7fbd;
  --navy:#2c4f86;
  --pale:#c6e0ea;
  --footer:#3a4c62;
  --footer-dark:#324257;
  --white:#fff;
}
*{box-sizing:border-box;margin:0;padding:0}
html,body{width:1200px;height:3896px;overflow:hidden;background:var(--white)}
body{position:relative;font-family:"Open Sans",Arial,sans-serif;color:var(--ink)}
.abs{position:absolute}
/* header */
.site-header{left:0;top:0;width:1200px;height:117px;background:#fff}
.brand{left:75px;top:30px;display:flex;align-items:center;gap:12px;font-family:"Cormorant Garamond",Georgia,serif;font-size:36px;font-weight:500;color:var(--navy)}
.brand .dot{width:22px;height:22px;border-radius:50%;background:var(--navy)}
.btn-top{top:38px;height:40px;font-family:"Oswald",Arial,sans-serif;font-size:17px;letter-spacing:.5px;display:flex;align-items:center;justify-content:center}
.btn-top.request{left:688px;width:228px;background:var(--teal);color:#fff}
.btn-top.call{left:925px;width:200px;border:2px solid var(--orange);color:var(--orange)}
.main-nav{left:0;top:117px;width:1200px;height:39px;background:var(--nav);display:flex;padding-left:72px;gap:30px;align-items:center}
.main-nav a{color:#fff;text-decoration:none;font-family:"Oswald",Arial,sans-serif;font-size:16px;letter-spacing:.4px}
/* hero */
.hero{left:0;top:156px;width:1200px;height:545px;background:linear-gradient(100deg,#9fb7c8 0%,#c9d8e2 30%,#e6eef3 60%,#d6e1e8 100%)}
.hero-tag{left:597px;top:377px;width:603px;height:117px;background:rgba(255,255,255,.85);padding:18px 15px;font-family:"Cormorant Garamond",Georgia,serif;font-size:35px;line-height:42px;color:#23496b}
.hero-shade{left:0;top:591px;width:1200px;height:110px;background:rgba(120,130,140,.35)}
.btn-hero{top:615px;height:65px;font-family:"Oswald",Arial,sans-serif;font-size:24px;color:#fff;display:flex;align-items:center;justify-content:center;gap:18px;box-shadow:0 3px 6px rgba(0,0,0,.25)}
.btn-hero.request{left:260px;width:330px;background:var(--teal)}
.btn-hero.call{left:610px;width:330px;background:var(--orange)}
/* section titles */
.title{left:0;width:1200px;text-align:center;font-family:"Cinzel",Georgia,serif;color:var(--teal);font-weight:400}
.title .sub{display:block;font-size:22px;line-height:24px}
.title .main{display:block;font-size:46px;line-height:50px}
.rule{left:500px;width:200px;height:14px}
.copy{left:90px;width:1020px;text-align:center;font-size:14px;line-height:24px;color:var(--muted)}
/* circles */
.value{top:974px;width:273px;height:273px;border-radius:50%;display:flex;flex-direction:column;align-items:center;justify-content:center;color:#fff;font-size:20px;line-height:26px;text-align:center;padding:0 40px}
.value .mark{width:42px;height:42px;border-radius:50%;border:3px solid rgba(255,255,255,.85);margin-bottom:14px}
.value.one{left:155px;background:#7f9cb6}
.value.two{left:461px;background:#5cbfd3}
.value.three{left:765px;background:#77d3cc}
/* experts */
.experts{left:0;top:1454px;width:1200px;height:468px}
.experts-photo{left:0;top:1466px;width:600px;height:440px;background:linear-gradient(90deg,#8fb4cf 0%,#b5cddd 45%,#cddbe4 100%)}
.experts-text{left:612px;top:1545px;width:530px}
.experts-text h2{font-family:"Cinzel",Georgia,serif;font-weight:400;font-size:33px;color:#2b4a6b;line-height:40px;margin-bottom:12px;white-space:nowrap}
.experts-text p{font-size:13.5px;line-height:22px;color:#2f4454;margin-bottom:18px}
/* why us */
.why-photo{left:600px;top:2430px;width:600px;height:700px;background:linear-gradient(90deg,rgba(44,79,134,0) 0%,rgba(110,140,180,.55) 50%,rgba(44,79,134,.2) 100%)}
.why-title{top:2445px;color:#fff}
.why-list{left:73px;top:2532px;width:545px;height:571px;background:#fff;border-radius:4px;padding:22px 26px;list-style:none;box-shadow:0 4px 10px rgba(0,0,0,.25)}
.why-list li{position:relative;padding-left:26px;font-size:14px;line-height:21px;color:#2f3b4a;padding-bottom:12px;margin-bottom:12px;border-bottom:1px solid #e4e8ec}
.why-list li:last-child{border-bottom:none}
.why-list li::before{content:"";position:absolute;left:0;top:4px;width:12px;height:12px;background:var(--nav);border-radius:2px}
/* actions */
.action-row{left:73px;top:3376px;width:1054px;height:208px;border-top:1px solid #e2e6ea;border-bottom:1px solid #e2e6ea;display:flex}
.action{flex:1;display:flex;flex-direction:column;align-items:center;justify-content:center;font-family:"Oswald",Arial,sans-serif;font-size:18px;line-height:20px;text-align:center;letter-spacing:.5px}
.action + .action{border-left:1px solid #e2e6ea}
.action .icon{width:91px;height:91px;border-radius:50%;display:flex;align-items:center;justify-content:center;margin-bottom:14px}
.action.request{color:var(--purple)} .action.request .icon{background:var(--purple)}
.action.reviews{color:var(--orange)} .action.reviews .icon{background:var(--orange)}
.action.call{color:var(--teal-dark)} .action.call .icon{background:var(--teal)}
/* footer */
.site-footer{left:0;top:3636px;width:1200px;height:213px;background:var(--footer);color:#fff}
.site-footer h4{font-family:"Oswald",Arial,sans-serif;font-weight:500;font-size:16px;letter-spacing:.5px;margin-bottom:14px}
.site-footer ul{list-style:none}
.site-footer li,.site-footer p{font-size:13px;line-height:21px}
.f-col{top:40px}
.social{display:flex;gap:10px}
.social span{width:36px;height:36px;background:#fff;display:block}
.footer-brand{left:835px;top:98px;display:flex;align-items:center;gap:10px;font-family:"Cormorant Garamond",Georgia,serif;font-size:30px;font-weight:500}
.footer-brand .dot{width:18px;height:18px;border-radius:50%;background:#fff}
.copyright{left:0;top:3849px;width:1200px;height:47px;background:var(--footer-dark);color:#dfe5ec;font-size:13px;display:flex;align-items:center;justify-content:center}
</style>
</head>
<body>

<header class="site-header abs">
  <div class="brand abs"><span class="dot"></span>Blue Pine Optics</div>
  <div class="btn-top request abs">REQUEST APPOINTMENT</div>
  <div class="btn-top call abs">CALL: 405 555 0142</div>
</header>
<nav class="main-nav abs">
  <a href="#">HOME</a><a href="#">VISION SERVICES</a><a href="#">VISION HEALTH</a><a href="#">PATIENT INFO</a><a href="#">PATIENT REVIEWS</a><a href="#">SCHEDULE APPOINTMENT</a><a href="#">CONTACT</a>
</nav>

<section class="hero abs" role="img" aria-label="Photo: close-up of an eye overlaid with a glowing digital vision-scan interface"></section>
<div class="hero-tag abs">Lorem ipsum dolor sit amet<br>Consectetur adipiscing elit</div>
<div class="hero-shade abs"></div>
<div class="btn-hero request abs">
  <svg width="28" height="28" viewBox="0 0 28 28"><rect x="2" y="5" width="24" height="21" rx="2" fill="#fff"/><rect x="2" y="5" width="24" height="6" fill="#d9f2f8"/><g fill="#1ea7c6"><rect x="6" y="14" width="4" height="3"/><rect x="12" y="14" width="4" height="3"/><rect x="18" y="14" width="4" height="3"/><rect x="6" y="19" width="4" height="3"/><rect x="12" y="19" width="4" height="3"/></g><rect x="7" y="2" width="3" height="6" fill="#fff"/><rect x="18" y="2" width="3" height="6" fill="#fff"/></svg>
  REQUEST APPOINTMENT
</div>
<div class="btn-hero call abs">
  <svg width="26" height="26" viewBox="0 0 24 24"><path fill="#fff" d="M6.6 10.8a15.1 15.1 0 0 0 6.6 6.6l2.2-2.2a1 1 0 0 1 1-.25 11.4 11.4 0 0 0 3.6.57 1 1 0 0 1 1 1V20a1 1 0 0 1-1 1A17 17 0 0 1 3 4a1 1 0 0 1 1-1h3.5a1 1 0 0 1 1 1c0 1.25.2 2.45.57 3.57a1 1 0 0 1-.25 1z"/></svg>
  CALL:405 555 0142
</div>

<h1 class="title abs" style="top:776px"><span class="sub">WELCOME TO</span><span class="main">BLUE PINE OPTICS</span></h1>
<svg class="rule abs" style="top:850px" viewBox="0 0 200 14"><line x1="0" y1="7" x2="85" y2="7" stroke="#1ea7c6"/><line x1="115" y1="7" x2="200" y2="7" stroke="#1ea7c6"/><circle cx="100" cy="7" r="5" fill="none" stroke="#1ea7c6"/></svg>
<p class="copy abs" style="top:888px;font-size:16px;line-height:26px">Sight is precious... Don't you think? We would love to have the opportunity to care foryour family's vision. Most of all, we want you to know that.....WE CARE!</p>

<div class="value one abs"><span class="mark"></span>Opening Your Eyes To Clearer Vision</div>
<div class="value two abs"><span class="mark"></span>A Personalized Approach To Vision Correction</div>
<div class="value three abs"><span class="mark"></span>Committed To Excellence In Vision Care</div>

<p class="copy abs" style="top:1292px">Our welcoming staff has one common goal - providing you with the best vision care possible and assisting you in finding you the finest eyewear that suits your lifestyle. While many big chain stores employ sales consultants to sell you glasses or contacts, our practice is comprised of knowledgeable individuals whose primary goal is to provide you with a high level of customer service all while ensuring you get the eye care you need and deserve.</p>

<svg class="experts abs" viewBox="0 0 1200 468" preserveAspectRatio="none">
  <polygon points="560,30 1200,0 1200,468 560,440" fill="#9ccbdc"/>
  <polygon points="580,20 1180,40 1160,440 600,455" fill="#cfe5ee"/>
  <polygon points="590,35 1170,50 1150,430 600,440" fill="#bddbe7"/>
</svg>
<div class="experts-photo abs" role="img" aria-label="Photo: macro close-up of a blue eye"></div>
<div class="experts-text abs">
  <h2>TRUE EXPERTS OF EYE CARE</h2>
  <p>Many people resort to the simple solution of purchasing glasses at a drug store or pharmacy, but it could cost them their vision.</p>
  <p>Our optometristsare skilled at not only detecting typical refractive errors (nearsightedness, farsightedness, and astigmatism) and prescribing the proper corrective eyewear, but also finding eye diseases in their early stages. You can't get that from a convenience store.</p>
  <p>Without regularly scheduled eye examinations, you may not realize that you are suffering from an eye disease until it affects your vision and may be more difficult to treat.</p>
</div>

<h2 class="title abs" style="top:2046px"><span class="main" style="font-size:40px">PERSONALIZED PATIENT CARE &amp; TREATMENT</span></h2>
<svg class="rule abs" style="top:2098px" viewBox="0 0 200 14"><line x1="0" y1="7" x2="85" y2="7" stroke="#1ea7c6"/><line x1="115" y1="7" x2="200" y2="7" stroke="#1ea7c6"/><circle cx="100" cy="7" r="5" fill="none" stroke="#1ea7c6"/></svg>
<div class="copy abs" style="top:2140px;color:#3a4450">
  <p>Refractive errors and other eye problems are common; however, not all ocular conditions are the same. At our practice, each patient is given a comprehensive eye examination, which allows our optometrist to get the whole picture of your eye health and find potential vision problems.</p>
  <p style="margin-top:18px">Only after carefully reviewing the findings of your exam, do we offer a treatment plan. If you do have a refractive error and are unsure of your options, our optometrist can help you decide between eyeglasses and contact lenses. We can also discuss the pros and cons of refractive surgery, like LASIK.</p>
  <p style="margin-top:18px">At our office, we take the time to give you the comprehensive vision treatment that you need and deserve.</p>
</div>

<svg class="abs" style="left:0;top:2376px" width="1200" height="780" viewBox="0 0 1200 780">
  <polygon points="0,20 1200,0 1200,70 0,60" fill="#a9cde0"/>
  <polygon points="0,44 1200,30 1200,750 0,779" fill="var(--navy)"/>
</svg>
<div class="why-photo abs" role="img" aria-label="Photo: coin-operated viewing binoculars at a lookout, tinted blue"></div>
<h2 class="title why-title abs"><span class="main" style="font-size:40px;color:#fff">WHY US?</span></h2>
<svg class="rule abs" style="top:2500px" viewBox="0 0 200 14"><line x1="0" y1="7" x2="85" y2="7" stroke="#fff"/><line x1="115" y1="7" x2="200" y2="7" stroke="#fff"/><circle cx="100" cy="7" r="5" fill="none" stroke="#fff"/></svg>
<ul class="why-list abs">
  <li>We treat you like a VIP - every experience you have with us will leave you knowing you received the VIP treatment</li>
  <li>We are here to serve YOU - we offer same day appointments and convenient clinic hours</li>
  <li>Our caring doctors are experts in eye care including advanced contact lens fits and the treatment of eye diseases</li>
  <li>We have the best trained and friendliest staff devoted to your care</li>
  <li>We offer the latest in eye care technology including the Lumeris Scan OCT, the Retiview retinal exam, and Clarion high-definition eyeglass lenses</li>
  <li>We are providers for most insurance plans</li>
  <li>We have strong relationships and network with the very best retinal, corneal, cataract, and LASIK surgeons in the state</li>
  <li>We have the Lumeris Field which provides the earliest detection of visual field loss</li>
</ul>

<h2 class="title abs" style="top:3240px"><span class="main" style="font-size:40px">THE HEALTH OF YOUR EYES IS OUR TOP PRIORITY!</span></h2>
<p class="copy abs" style="top:3296px;font-size:16px;color:#3a4450">Please <span style="color:var(--teal)">Contact Us</span> if you have any questions, need additional information.</p>

<div class="action-row abs">
  <div class="action request"><span class="icon"><svg width="40" height="40" viewBox="0 0 28 28"><rect x="2" y="5" width="24" height="21" rx="2" fill="#fff"/><g fill="#3a2f8f"><rect x="6" y="13" width="4" height="3"/><rect x="12" y="13" width="4" height="3"/><rect x="18" y="13" width="4" height="3"/><rect x="6" y="19" width="4" height="3"/><rect x="12" y="19" width="4" height="3"/></g></svg></span>REQUEST<br>APPOINTMENT</div>
  <div class="action reviews"><span class="icon"><svg width="44" height="44" viewBox="0 0 24 24"><path fill="#fff" d="M12 2l2.9 6.9 7.1.6-5.4 4.7 1.6 7L12 17.5 5.8 21.2l1.6-7L2 9.5l7.1-.6z"/></svg></span>READ<br>OUR REVIEWS</div>
  <div class="action call"><span class="icon"><svg width="40" height="40" viewBox="0 0 24 24"><path fill="#fff" d="M6.6 10.8a15.1 15.1 0 0 0 6.6 6.6l2.2-2.2a1 1 0 0 1 1-.25 11.4 11.4 0 0 0 3.6.57 1 1 0 0 1 1 1V20a1 1 0 0 1-1 1A17 17 0 0 1 3 4a1 1 0 0 1 1-1h3.5a1 1 0 0 1 1 1c0 1.25.2 2.45.57 3.57a1 1 0 0 1-.25 1z"/></svg></span>CALL<br>405-555-0142</div>
</div>

<footer class="site-footer abs">
  <div class="f-col abs" style="left:73px">
    <h4>QUICK LINKS</h4>
    <ul><li>Home</li><li>Vision Services</li><li>Vision Health</li><li>Patient Info</li></ul>
  </div>
  <div class="f-col abs" style="left:203px;top:75px">
    <ul><li>Patient Reviews</li><li>Schedule Appointment</li><li>Contact</li></ul>
  </div>
  <div class="f-col abs" style="left:400px">
    <h4>CONTACT US</h4>
    <p>1280 North Harlow Avenue<br>Oklahoma City, OK 73120<br>Phone: 405-555-0142<br>Fax: 405-555-0178<br>Contact Us Online!</p>
  </div>
  <div class="f-col abs" style="left:648px">
    <h4>FOLLOW US</h4>
    <div class="social"><span></span><span></span></div>
  </div>
  <div class="footer-brand abs"><span class="dot"></span>Blue Pine Optics</div>
</footer>
<div class="copyright abs">© 2016 Blue Pine Optics | All Rights Reserved | Privacy Policy</div>

</body>
</html>
```